kVista Corporate Website

kVista is a well-funded start up developing an Online Marketing Platform for small businesses in Europe.
We are launching in February 2012 with all-in-one online marketing services including professional website, DIY SEO, Dashboard with Reports and Online marketing tools, and Support.
Our internal web designer has come up with a preliminary website design which we wish to continue to improve using new ideas, colours, layout, image, etc.
The brief is very simple - improve the website whether it is look & feel, ease of use, conversion rate - we are looking for overall improvements.
The contest will last 5 days and we will award the winner £300.
If you are the winner , you will also be required to provide designs for 3 more internal pages adhering to the proposed home page design.
Judging criteria : -
Visual Design
Layout must adhere to best practices and wire frame. If you decide to move elements around significantly please provide reason
Functional, informative and drives calls to action
Industry/Entity Type
Marketing
Look and feel
Each slider illustrates characteristics of the customer's brand and the style your logo design should communicate.

```html
<!DOCTYPE html>
<html lang="en">
<head>
<meta charset="utf-8">
<title>kVista – Online Marketing for Small Business Websites</title>
<link href="https://fonts.googleapis.com/css2?family=Arimo:wght@400;700&family=Open+Sans:wght@300;400;600&family=Oswald:wght@500;700&display=swap" rel="stylesheet">
<style>
:root{
  --sky:#d4e9f8;
  --page:#f4f6f9;
  --blue:#1e8fe0;
  --blue-deep:#0b63c4;
  --link:#1a8ad6;
  --ink:#222;
  --muted:#555;
  --dark:#1f1f1f;
  --footer:#262626;
  --orange:#f79a0e;
}
*{margin:0;padding:0;box-sizing:border-box}
html,body{width:803px;height:1200px;overflow:hidden}
body{position:relative;background:var(--page);font-family:Arimo,Arial,sans-serif;color:var(--ink)}
.abs{position:absolute}
.sky-band{left:0;top:0;width:803px;height:429px;background:var(--sky);border-top:4px solid var(--dark)}
.top-nav{left:536px;top:0;width:160px;height:21px;background:var(--dark);border-radius:0 0 10px 10px;display:flex;justify-content:space-around;align-items:center;font-size:7px;font-weight:700;color:#fff;letter-spacing:.2px}
.brand{left:106px;top:38px;display:flex;align-items:center;gap:6px}
.brand-dot{width:44px;height:44px;border-radius:50%;background:var(--blue)}
.brand-name{font-family:"Open Sans",sans-serif;font-weight:400;font-size:42px;color:#111;line-height:1}
.like{left:302px;top:73px;display:flex;gap:3px;font-size:7px}
.like span{border:1px solid #b8c4d4;background:#eef2f7;padding:1px 3px;color:#3b5998}
.like span+span{color:#333;background:#fff}
.main-nav{left:538px;top:59px;width:156px;height:24px;border-radius:5px;background:linear-gradient(#f3f3f3,#cfcfcf);display:flex;align-items:center;font-size:9px;font-weight:700;color:#222;overflow:hidden}
.main-nav .home{width:38px;height:100%;background:linear-gradient(#36a4f2,#0a6fd0);display:flex;align-items:center;justify-content:center}
.main-nav .item{padding:0 9px;border-right:1px solid #b5b5b5}
.main-nav .item:last-child{border:0}
.hero{left:102px;top:106px;width:600px;height:230px;border-radius:5px;border:2px solid #fff;background:radial-gradient(ellipse at 20% 20%,#7fd0ff,#2a9af0 45%,#0b75db);box-shadow:0 14px 14px -8px rgba(0,0,0,.25);overflow:hidden}
.hero h1{position:absolute;left:29px;top:10px;font-size:21px;line-height:23px;color:#fff;font-weight:700;text-shadow:0 1px 2px rgba(0,40,110,.6)}
.hero ul{position:absolute;left:29px;top:73px;list-style:none}
.hero li{color:#fff;font-weight:700;font-size:13.5px;height:22.5px;display:flex;align-items:center;gap:14px;text-shadow:0 1px 1px rgba(0,40,110,.5)}
.cta{position:absolute;left:68px;top:175px;width:104px;height:37px;border-radius:5px;background:linear-gradient(#ffc02a,#f08500);border:1px solid #ffd36b;color:#fff;text-align:center;font-weight:700;box-shadow:0 2px 3px rgba(0,0,0,.25)}
.cta small{display:block;font-size:8px;font-weight:400;margin-top:4px}
.cta b{font-size:16px}
.hero-person{position:absolute;left:410px;top:78px;width:190px;height:152px;background:radial-gradient(circle at 60% 30%,#e2b79a 0 22%,#4f74b8 23%,#2d59a8 70%);opacity:.9}
.tag{position:absolute;background:#fff;color:#333;font-size:6.5px;padding:2px 7px;border-radius:1px;box-shadow:0 1px 2px rgba(0,0,0,.2);white-space:nowrap}
.headline{left:0;width:803px;top:371px;text-align:center;font-family:"Open Sans",sans-serif;font-weight:300;font-size:19px;color:#222}
.headline em{font-style:normal;color:var(--blue-deep)}
.headline p{font-size:13px;margin-top:0;color:#333}
.offer{top:453px;width:139px;height:93px;border-radius:3px;box-shadow:0 3px 4px rgba(0,0,0,.3);color:#fff;font-family:Oswald,sans-serif;padding:8px 10px;overflow:hidden}
.offer .big{font-size:22px;line-height:22px;font-weight:700;text-transform:uppercase}
.offer .accent{color:#ffe600}
.offer .sub{position:absolute;left:0;bottom:0;width:100%;text-align:center;font-size:10px;font-weight:500;padding:3px 0}
.offer .ribbon{position:absolute;right:-18px;top:12px;transform:rotate(45deg);background:#e8372a;font-size:9px;padding:2px 20px;border-top:2px solid #fff}
.offer-red{left:106px;background:linear-gradient(#f22a20,#a60b0b)}
.offer-orange{left:255px;background:linear-gradient(135deg,#ffb400,#e3420b)}
.offer-green{left:402px;background:linear-gradient(135deg,#5fcd2a,#137a13)}
.offer-red .sub{background:#5b0606}
.offer-orange .sub{background:#7a2c07}
.how{left:550px;top:453px;width:139px;height:93px;background:linear-gradient(#fff,#dcdcdc);border:1px solid #ccc;border-radius:3px;box-shadow:0 3px 4px rgba(0,0,0,.3);padding:8px 9px;font-size:8px;color:#333;line-height:11.5px}
.how h3{font-family:Oswald,sans-serif;font-size:11px;font-weight:500;margin-bottom:3px}
.how p{font-style:italic;text-align:justify;padding-left:1px}
.section-title{font-family:"Open Sans",sans-serif;font-weight:400;color:var(--link)}
.about{left:106px;top:580px;width:290px}
.about h2{font-size:18px;display:flex;align-items:center;gap:6px;padding-left:1px}
.about h2 i{width:17px;height:17px;border-radius:50%;border:3px solid #7dbfe9}
.about p{font-size:7.6px;line-height:11.3px;color:#444;text-align:justify;margin-top:4px}
.about p+p{margin-top:11px}
.link{color:var(--link)}
.more{font-size:8px;color:var(--link);display:flex;align-items:center;gap:5px}
.more::before{content:"";width:7px;height:7px;border-radius:50%;border:1px solid #9bb}
.feature{width:102px}
.feature h3{font-size:13px;margin-bottom:6px;white-space:nowrap}
.feature p{font-size:7.4px;line-height:9.5px;color:#555}
.feature svg{position:absolute;left:-35px;top:10px}
.shadow-line{left:110px;top:764px;width:583px;height:14px;background:radial-gradient(ellipse at center,rgba(0,0,0,.12),transparent 70%)}
.examples{left:108px;top:824px;width:587px;height:132px;background:#f3f3f3;border:1px solid #e1e1e1;border-radius:6px;overflow:hidden}
.examples .arrow{position:absolute;top:0;width:22px;height:100%;background:#d9d9d9;display:flex;align-items:center;justify-content:center;color:#2b95e0;font-size:11px}
.examples h3{position:absolute;left:34px;top:14px;font-size:11px;line-height:11.5px;font-family:Arimo,sans-serif;color:#1b87d6;font-weight:400}
.examples p{position:absolute;left:34px;top:48px;width:135px;font-size:7.4px;line-height:10.8px;color:#444}
.examples .more{position:absolute;left:120px;top:115px;font-size:7.5px}
.thumb{position:absolute;top:9px;height:117px;box-shadow:0 1px 3px rgba(0,0,0,.3)}
.footer{left:0;top:985px;width:803px;height:215px;background:linear-gradient(#2b2b2b,#1c1c1c);color:#ccc}
.fcol{position:absolute;top:24px}
.fcol h4{font-family:"Open Sans",sans-serif;font-weight:400;font-size:12px;color:#2fa4ef;display:flex;align-items:center;gap:10px;height:24px;border-bottom:1px solid #3a3a3a;padding-bottom:4px}
.fcol ul{list-style:none;margin-top:6px}
.fcol li{font-size:7.2px;height:18.7px;line-height:18.7px;border-bottom:1px solid #3a3a3a;padding-left:8px;position:relative;color:#ccc}
.fcol li::before{content:"›";position:absolute;left:0;color:#2fa4ef}
.subscribe{position:absolute;left:598px;top:61px;width:100px;height:16px;background:#fff;border-radius:2px;font-size:6.5px;color:#aaa;font-style:italic;padding:4px 4px;border-right:18px solid var(--blue)}
.follow{position:absolute;left:599px;top:101px;font-family:"Open Sans",sans-serif;font-size:12px;color:#2fa4ef}
.social{position:absolute;top:119px;width:20px;height:20px;border-radius:50%;background:#f0f0f0}
.copy{position:absolute;left:0;top:180px;width:100%;text-align:center;font-size:7.2px;color:#ccc}
.copy span{color:#2fa4ef}
</style>
</head>
<body>
<div class="abs sky-band"></div>
<nav class="abs top-nav"><span>ABOUT US</span><span>CONTACT US</span><span>LOGIN</span></nav>

<div class="abs brand"><span class="brand-dot"></span><span class="brand-name">kVista</span></div>
<div class="abs like"><span>Like</span><span>62</span></div>

<nav class="abs main-nav">
  <span class="home"><svg width="16" height="14" viewBox="0 0 16 14"><path d="M8 1 1 7h2v6h4V9h2v4h4V7h2z" fill="#fff"/></svg></span>
  <span class="item">Quick Tour</span><span class="item">Pricing</span>
</nav>

<section class="abs hero">
  <h1>Getting a website has never<br>been so simple</h1>
  <ul>
    <li><svg width="16" height="12" viewBox="0 0 16 12"><path d="M0 4h9V0l7 6-7 6V8H0z" fill="#fff"/></svg>Business Websites</li>
    <li><svg width="16" height="12" viewBox="0 0 16 12"><path d="M0 4h9V0l7 6-7 6V8H0z" fill="#fff"/></svg>Online Marketing</li>
    <li><svg width="16" height="12" viewBox="0 0 16 12"><path d="M0 4h9V0l7 6-7 6V8H0z" fill="#fff"/></svg>Dashboard Controls</li>
    <li><svg width="16" height="12" viewBox="0 0 16 12"><path d="M0 4h9V0l7 6-7 6V8H0z" fill="#fff"/></svg>Full Setup &amp; Support</li>
  </ul>
  <a class="cta"><small>Sign up NOW for</small><b>FREE!</b></a>
  <div class="hero-person" role="img" aria-label="Photo of a puzzled businessman scratching his head"></div>
  <span class="tag" style="left:307px;top:91px">PPC</span>
  <span class="tag" style="left:397px;top:81px">Testimonials</span>
  <span class="tag" style="left:458px;top:83px">Hosting</span>
  <span class="tag" style="left:520px;top:86px;padding:2px 4px">Content Management</span>
  <span class="tag" style="left:390px;top:100px">Deals</span>
  <span class="tag" style="left:483px;top:102px">Website Design</span>
  <span class="tag" style="left:541px;top:105px">Reporting</span>
  <span class="tag" style="left:335px;top:113px">Email Marketing</span>
  <span class="tag" style="left:440px;top:112px">Images</span>
  <span class="tag" style="left:390px;top:124px">Search Ads</span>
  <span class="tag" style="left:320px;top:135px">Directories</span>
  <span class="tag" style="left:420px;top:138px">SEO</span>
  <span class="tag" style="left:367px;top:148px">Blogs /News</span>
  <span class="tag" style="left:418px;top:164px">Referrals</span>
  <span class="tag" style="left:345px;top:170px">Social Pages</span>
  <span class="tag" style="left:386px;top:185px">Micro Feeds</span>
</section>

<div class="abs headline">The Complete Online Marketing Solution for <em>Small Business Websites</em>
  <p>“Get a big online presence and more sales leads in 30 minutes”</p></div>

<div class="abs offer offer-red"><div class="big accent">Free</div><div class="big">Setup</div><span class="ribbon">£199</span><div class="sub" style="font-size:13px">WEB OFFER ONLY</div></div>
<div class="abs offer offer-orange"><div class="big accent">Pro</div><div class="big">Package</div><span class="ribbon">£22</span><div class="sub">Business Website &amp; Easy Dashboard</div></div>
<div class="abs offer offer-green"><div class="big" style="font-size:17px;line-height:20px">Turbo Sales<br>Pro Plus</div><div style="font-size:8px;color:#ffe600">More sales LEADS</div><span class="ribbon">£29</span><div class="sub" style="line-height:12px">Bussiness Website,<br>Easy Dashboard &amp; ppc Sales</div></div>
<div class="abs how"><h3>How does it work?</h3><p>Neque porro quisquam est qui dolorem ipsum quia dolor sit amet, consectetur, adipisci velit”</p></div>

<section class="abs about">
  <h2 class="section-title"><i></i>About Us</h2>
  <p><span class="link">kVista</span> will build your business website, optimise SEO marketing and make recommendations on best practices to help you win customers. Let our team of experts design a business website for you. Choose a business website from <span class="link">kVista's</span> broad array of fabulous, customisable business websites and our experts will have your business online in minutes. <span class="link">kVista</span> lets you create a professional business website without the need to know how to code or programme.</p>
  <p>Your business website comes with automatic Internet marketing, marketing on the Internet is easy with <span class="link">kVista</span>, we automatically optimise your site for SEO marketing and we can run search ad campaigns when you need them.</p>
</section>
<a class="abs more" style="left:340px;top:729px">Read more</a>

<div class="abs feature" style="left:443px;top:581px"><h3 class="section-title">Case Studies</h3><p>Read real stories about small businesses online</p>
  <svg width="26" height="26" viewBox="0 0 26 26"><path d="M2 24V6h5v18zM9 24V12h5v12zM16 24v-8h5v8zM1 25h24" fill="#bbb" stroke="#aaa"/></svg></div>
<div class="abs feature" style="left:588px;top:581px;width:112px"><h3 class="section-title">How to</h3><p>Learn from our online marketing tips for small business</p>
  <svg width="22" height="28" viewBox="0 0 22 28"><circle cx="11" cy="10" r="8" fill="none" stroke="#bbb" stroke-width="2"/><path d="M7 20h8v5H7z" fill="#bbb"/></svg></div>
<div class="abs feature" style="left:445px;top:675px"><h3 class="section-title">News &amp; Chatter</h3><p>Get up-to-date news and chatter about online marketing</p>
  <svg width="30" height="26" viewBox="0 0 30 26"><path d="M2 3h18v12H8l-5 4v-4H2z" fill="#bbb"/><path d="M12 10h16v11h-2v4l-5-4h-9z" fill="#999"/></svg></div>
<div class="abs feature" style="left:590px;top:675px;width:110px"><h3 class="section-title">Demo</h3><p>Find out what kVista can do for your business.</p>
  <svg width="28" height="28" viewBox="0 0 28 28"><circle cx="14" cy="15" r="11" fill="#bbb"/><circle cx="14" cy="15" r="8" fill="#ddd"/><path d="M14 15V9M12 2h4" stroke="#888" stroke-width="2"/></svg></div>

<div class="abs shadow-line"></div>

<section class="abs examples">
  <span class="arrow" style="left:0">◀</span><span class="arrow" style="right:0">▶</span>
  <h3>View examples of our<br>stunning business websites</h3>
  <p>Duis autem vel eum iriure dolor in hendrerit in vulputate velit esse molestie consequat, vel illum dolore eu feugiat nulla facilisis at vero eros et accumsan. esse molestie.</p>
  <a class="more">View more</a>
  <div class="thumb" role="img" aria-label="Example website screenshot with purple header" style="left:184px;width:80px;background:linear-gradient(#2c2450 0 10%,#f3f0f4 10%,#e7e0e8)"></div>
  <div class="thumb" role="img" aria-label="Example website screenshot with blue sky header" style="left:279px;width:81px;background:linear-gradient(#8ccbf0,#e9f3fb 55%,#1b1b1b 80%)"></div>
  <div class="thumb" role="img" aria-label="Example website screenshot with dark theme" style="left:375px;width:86px;background:linear-gradient(#2a2a2a,#3a3a3a 40%,#222)"></div>
  <div class="thumb" role="img" aria-label="Example website screenshot with pink and blue gradient" style="left:475px;width:80px;background:linear-gradient(160deg,#d81a7c,#6b2a9a 50%,#1d4fc2)"></div>
</section>

<footer class="abs footer">
  <div class="fcol" style="left:109px;width:138px">
    <h4><svg width="20" height="20" viewBox="0 0 20 20"><circle cx="10" cy="10" r="7" fill="none" stroke="#777" stroke-width="4" stroke-dasharray="3 2"/><circle cx="10" cy="10" r="3" fill="#777"/></svg>OurServices</h4>
    <ul><li>Search Engine Optimization (SEO)</li><li>Social Media</li><li>Web Analytics</li></ul>
  </div>
  <div class="fcol" style="left:298px;width:99px">
    <h4><svg width="22" height="24" viewBox="0 0 22 24"><rect x="2" y="1" width="18" height="22" rx="3" fill="#777"/><rect x="5" y="4" width="12" height="14" fill="#333"/></svg>ContactUs</h4>
    <ul><li>Contact Us</li><li>Customer Support</li><li>Request a call back</li><li>FAQ's</li></ul>
  </div>
  <div class="fcol" style="left:447px;width:100px">
    <h4><svg width="28" height="20" viewBox="0 0 28 20"><path d="M1 3h9l2 3h14v13H1z" fill="#777"/></svg>Navigation</h4>
    <ul><li>Site Map</li><li>Terms and Condition</li><li>Privacy &amp; Policy</li><li>Get in Touch</li></ul>
  </div>
  <div class="fcol" style="left:597px;width:101px">
    <h4><svg width="28" height="20" viewBox="0 0 28 20"><rect x="1" y="2" width="26" height="16" fill="#777"/><path d="M1 2l13 10L27 2" fill="none" stroke="#444" stroke-width="1.5"/></svg>Subscribe</h4>
  </div>
  <div class="subscribe">Type your email here</div>
  <div class="follow">Follow</div>
  <span class="social" style="left:600px"></span>
  <span class="social" style="left:630px"></span>
  <span class="social" style="left:661px"></span>
  <p class="copy">Copyright © 2011 kVista Pvt. Ltd 2011 - &nbsp;All rights reserved. &nbsp;Managed by <span>kVista</span> &nbsp; I &nbsp; Admin</p>
</footer>
</body>
</html>
```